UX Design for Analytics Web Application

http://tovelunigroup.com/
We are tech & consulting company with analytics products (web applications), located at Rio de Janeiro, Brazil.

We are searching a partner do develop UX for our products, i.e, aesthetics, usability, HTML/CSS.

Currently we have a product suite and the goal is to make a pilot re-design project with one of our products.

The product of interest is interactive webapp that aims at data analysis, significantly different from blogs, e-commerce or landing pages.

We do have a software development team but we lack an UX & HTML expert. Currently we use Bootstrap templates but the results are insatisfatory.

So, the project scope is, to develop the arts (UX, aesthetics, etc) along with the code/mockup (HTML/CSS) for one of our product (3 pages).

This is a pilot project and there's potential to rehire for our other products. Code quality is of importance.

More details and specification can be found in attached files.

Target Market(s)

Executives, managers & consultants

Industry/Entity Type

It Company

Coding

Coded - Design and coding required

Number of Pages Required

3 page

Font styles to use
Sans Serif

Requirements
Must have
• (see attached files, prefer the pptx version))
• -Responsive
Nice to have
• (see attached files, prefer the pptx version)
Should not have
• -Avoid Green, Red and Yellow colors. They have a meaning of good, bad and average in our products.

```html
<!DOCTYPE html>
<html lang="en">
<head>
<meta charset="utf-8">
<title>TOVELU-METRA · Processes Dashboard</title>
<link rel="stylesheet" href="https://fonts.googleapis.com/css2?family=Lato:wght@400;700&display=swap">
<style>
  :root {
    --navy: #2f3240;
    --brown: #a9603c;
    --tan: #e0bfa2;
    --sky: #6fa8dc;
    --mist: #e4e4e4;
    --header-bg: #f1f1f1;
    --footer-bg: #4a4a4a;
    --line: #dcdcdc;
    --text: #3a3a3a;
    --muted: #555;
    --white: #fff;
  }
  * { box-sizing: border-box; margin: 0; padding: 0; }
  html, body { width: 1200px; height: 480px; overflow: hidden; }
  body {
    position: relative;
    background: var(--white);
    font-family: "Lato", Arial, sans-serif;
    color: var(--text);
  }
  .abs { position: absolute; }

  /* Header */
  .app-header { left: 0; top: 0; width: 1200px; height: 43px; background: var(--header-bg); border-bottom: 1px solid #e2e2e2; }
  .menu-toggle { left: 262px; top: 13px; width: 20px; height: 17px; }
  .menu-toggle span { display: block; height: 3px; background: var(--navy); border-radius: 2px; margin-bottom: 4px; }
  .brand { left: 293px; top: 12px; display: flex; align-items: center; gap: 5px; }
  .brand-dot { width: 16px; height: 16px; border-radius: 50%; background: var(--brown); }
  .brand-name { font-size: 16px; font-weight: 700; color: var(--navy); letter-spacing: .2px; }
  .header-action { top: 9px; width: 25px; height: 25px; border-radius: 50%; display: flex; align-items: center; justify-content: center; }
  .header-action.notifications { left: 847px; background: var(--navy); }
  .header-action.profile { left: 880px; background: var(--brown); }
  .header-action.settings { left: 912px; background: var(--tan); }

  /* Panels */
  .panel { background: var(--white); border: 1px solid var(--line); }
  .summary { left: 262px; top: 58px; width: 429px; height: 151px; }
  .summary-title { left: 24px; top: 20px; font-size: 14.5px; font-weight: 700; color: #444; }
  .metric { left: 24px; color: #444; }
  .metric b { font-weight: 700; color: var(--navy); }
  .metric.spent { top: 65px; font-size: 13px; }
  .metric.gap { top: 91px; font-size: 10.5px; }
  .metric.gap em { font-style: normal; font-weight: 700; color: var(--brown); }
  .metric.negotiated { top: 116px; font-size: 8px; }
  .metric.negotiated em { font-style: normal; color: var(--tan); }
  .metric-bar { left: 144px; height: 14px; font-size: 8px; font-weight: 700; color: var(--white); display: flex; align-items: center; justify-content: flex-end; padding-right: 5px; }
  .metric-bar.spent { top: 67px; width: 122px; background: repeating-linear-gradient(135deg, var(--navy) 0 3px, #3b3f50 3px 5px); }
  .metric-bar.gap { top: 91px; width: 36px; background: var(--brown); }
  .metric-bar.negotiated { top: 114px; width: 31px; background: var(--tan); }
  .completion-chart { left: 307px; top: 22px; }
  .completion-label { left: 300px; top: 117px; width: 106px; text-align: center; font-size: 14.5px; font-weight: 700; color: #444; }
  .completion-label sup { font-size: 7px; }

  /* Activity */
  .activity { left: 704px; top: 58px; width: 234px; height: 151px; }
  .activity-item { left: 10px; width: 212px; height: 38px; display: flex; align-items: center; gap: 9px; border-bottom: 1px solid #e6e6e6; }
  .activity-item svg { flex: none; }
  .activity-item p { font-size: 6.6px; line-height: 1.4; color: var(--muted); }
  .activity-item a { color: var(--muted); }
  .activity-item .when { margin-left: 5px; }
  .see-all { left: 9px; top: 118px; width: 213px; height: 21px; background: #eee; border: 1px solid #cfcfcf; border-radius: 2px; font-size: 10.5px; text-align: center; line-height: 19px; color: #333; }

  /* Toolbar */
  .toolbar { left: 262px; top: 222px; width: 676px; height: 46px; display: flex; align-items: center; }
  .toolbar-item { flex: 1; text-align: center; font-size: 13px; color: #444; }
  .toolbar-item + .toolbar-item { border-left: 1px solid var(--line); }

  /* Processes */
  .processes { left: 262px; top: 281px; width: 676px; height: 152px; }
  .process-card { top: 13px; width: 209px; height: 123px; border: 1px solid #e8e8e8; background: var(--white); }
  .process-cover { left: 0; top: 0; width: 100%; height: 50px; }
  .cover-sunset { background: linear-gradient(180deg, #7a5a1f 0%, #c9931f 60%, #e0b040 100%); }
  .cover-hall { background: linear-gradient(180deg, #5a5650 0%, #8d857a 55%, #3e3a35 100%); }
  .cover-rest { background: linear-gradient(160deg, #6d4b38 0%, #9a7a64 55%, #3a2a22 100%); }
  .process-title { left: 11px; top: 27px; font-size: 12.5px; font-weight: 700; color: var(--white); letter-spacing: -.2px; }
  .process-toggle { left: 12px; top: 61px; }
  .process-amount { left: 41px; top: 56px; font-size: 12.5px; line-height: 16px; }
  .process-note { left: 12px; top: 93px; font-size: 7.6px; line-height: 11px; color: #444; }
  .process-note a { color: #444; }
  .process-note b { font-weight: 700; }
  .process-mix { left: 128px; top: 60px; }
  .tone-navy { color: var(--navy); }
  .tone-brown { color: var(--brown); }
  .tone-tan { color: var(--tan); }

  /* Footer */
  .app-footer { left: 0; top: 446px; width: 1200px; height: 34px; background: var(--footer-bg); }
  .footer-brand { left: 886px; top: 10px; display: flex; align-items: center; gap: 4px; }
  .footer-brand .brand-dot { width: 12px; height: 12px; background: var(--white); }
  .footer-brand .brand-name { font-size: 12.5px; color: var(--white); }
</style>
</head>
<body>

<header class="app-header abs">
  <div class="menu-toggle abs"><span></span><span></span><span></span></div>
  <div class="brand abs"><span class="brand-dot"></span><span class="brand-name">TOVELU-METRA</span></div>
  <div class="header-action notifications abs">
    <svg width="12" height="13" viewBox="0 0 12 13"><path d="M6 1a3.5 3.5 0 0 0-3.5 3.5V8L1 10h10L9.5 8V4.5A3.5 3.5 0 0 0 6 1z" fill="#fff"/><circle cx="6" cy="11.5" r="1.3" fill="#fff"/></svg>
  </div>
  <div class="header-action profile abs">
    <svg width="12" height="12" viewBox="0 0 12 12"><circle cx="6" cy="3.5" r="2.8" fill="#fff"/><path d="M0.5 12a5.5 4.5 0 0 1 11 0z" fill="#fff"/></svg>
  </div>
  <div class="header-action settings abs">
    <svg width="13" height="13" viewBox="0 0 13 13"><circle cx="6.5" cy="6.5" r="4" fill="none" stroke="#fff" stroke-width="2.4" stroke-dasharray="1.6 1.2"/><circle cx="6.5" cy="6.5" r="3.2" fill="#fff"/><circle cx="6.5" cy="6.5" r="1.3" fill="var(--tan)"/></svg>
  </div>
</header>

<section class="summary panel abs">
  <h2 class="summary-title abs">14 Active Processes</h2>
  <p class="metric spent abs">31 millions <b>expent</b></p>
  <div class="metric-bar spent abs">?</div>
  <p class="metric gap abs">with 2 millions of <em>gap</em></p>
  <div class="metric-bar gap abs">6%</div>
  <p class="metric negotiated abs">and 1.5 million <em>negotiated</em></p>
  <div class="metric-bar negotiated abs">5%</div>
  <svg class="completion-chart abs" width="92" height="92" viewBox="0 0 92 92" aria-label="72% completed">
    <g transform="rotate(-90 46 46)" fill="none" stroke-width="18">
      <circle cx="46" cy="46" r="36" pathLength="100" stroke="var(--navy)" stroke-dasharray="72 28"/>
      <circle cx="46" cy="46" r="36" pathLength="100" stroke="var(--brown)" stroke-dasharray="0 72 14 14"/>
      <circle cx="46" cy="46" r="36" pathLength="100" stroke="var(--tan)" stroke-dasharray="0 86 14 0"/>
    </g>
  </svg>
  <p class="completion-label abs">72<sup>%</sup> completed</p>
</section>

<aside class="activity panel abs">
  <div class="activity-item abs" style="top:6px">
    <svg width="20" height="20" viewBox="0 0 20 20"><circle cx="10" cy="10" r="8.5" fill="none" stroke="var(--navy)" stroke-width="3"/></svg>
    <p><a href="#">Lena Marsh</a> upload new data with 23823 rows to the <a href="#">XPTO Process</a> and he is happy now <span class="when">- 2 days ago</span></p>
  </div>
  <div class="activity-item abs" style="top:44px">
    <svg width="20" height="20" viewBox="0 0 20 20"><rect x="1.5" y="1.5" width="17" height="17" fill="none" stroke="var(--brown)" stroke-width="3"/></svg>
    <p><a href="#">Pia Oren</a> started the <a href="#">ABC process</a> <span class="when">- 2 days ago</span></p>
  </div>
  <div class="activity-item abs" style="top:82px">
    <svg width="20" height="20" viewBox="0 0 20 20"><path d="M10 2L18.5 18H1.5z" fill="none" stroke="var(--tan)" stroke-width="3" stroke-linejoin="miter"/></svg>
    <p><a href="#">Rui Calden</a> is making a new content layout specification <span class="when">- 2 days ago</span></p>
  </div>
  <div class="see-all abs">Sell all</div>
</aside>

<nav class="toolbar panel abs">
  <div class="toolbar-item">Search</div>
  <div class="toolbar-item">Sort By</div>
  <div class="toolbar-item">Filter By</div>
  <div class="toolbar-item">Add Process</div>
</nav>

<section class="processes panel abs">
  <article class="process-card abs" style="left:12px">
    <div class="process-cover cover-sunset abs" role="img" aria-label="Photo of a sunset over a field with power lines"></div>
    <h3 class="process-title abs">Process Buy A Dount</h3>
    <svg class="process-toggle abs" width="24" height="24" viewBox="0 0 24 24"><circle cx="12" cy="12" r="11" fill="none" stroke="var(--navy)" stroke-width="1.6"/><path d="M7.5 10l4.5 4.5 4.5-4.5" fill="none" stroke="var(--navy)" stroke-width="1.8"/></svg>
    <p class="process-amount tone-navy abs">14 million<br>in expenses</p>
    <p class="process-note abs">Some short free text with<br><a href="#">links</a> and <b>13,432 number</b></p>
    <svg class="process-mix abs" width="56" height="56" viewBox="0 0 56 56">
      <g transform="rotate(-90 28 28)" fill="none" stroke-width="12">
        <circle cx="28" cy="28" r="21" pathLength="100" stroke="var(--navy)" stroke-dasharray="25 75"/>
        <circle cx="28" cy="28" r="21" pathLength="100" stroke="var(--brown)" stroke-dasharray="0 25 25 50"/>
        <circle cx="28" cy="28" r="21" pathLength="100" stroke="var(--tan)" stroke-dasharray="0 50 21 29"/>
        <circle cx="28" cy="28" r="21" pathLength="100" stroke="var(--mist)" stroke-dasharray="0 71 15 14"/>
        <circle cx="28" cy="28" r="21" pathLength="100" stroke="var(--sky)" stroke-dasharray="0 86 14 0"/>
      </g>
    </svg>
  </article>

  <article class="process-card abs" style="left:234px">
    <div class="process-cover cover-hall abs" role="img" aria-label="Photo of an empty industrial hall with large windows"></div>
    <h3 class="process-title abs">Process Buy A Dount</h3>
    <svg class="process-toggle abs" width="24" height="24" viewBox="0 0 24 24"><circle cx="12" cy="12" r="11" fill="none" stroke="var(--brown)" stroke-width="1.6"/><path d="M7.5 14l4.5-4.5 4.5 4.5" fill="none" stroke="var(--brown)" stroke-width="1.8"/></svg>
    <p class="process-amount tone-brown abs">14 million<br>in expenses</p>
    <p class="process-note abs">Some short free text with<br><a href="#">links</a> and <b>13,432 number</b></p>
    <svg class="process-mix abs" width="56" height="56" viewBox="0 0 56 56">
      <g transform="rotate(-90 28 28)" fill="none" stroke-width="12">
        <circle cx="28" cy="28" r="21" pathLength="100" stroke="var(--navy)" stroke-dasharray="25 75"/>
        <circle cx="28" cy="28" r="21" pathLength="100" stroke="var(--brown)" stroke-dasharray="0 25 25 50"/>
        <circle cx="28" cy="28" r="21" pathLength="100" stroke="var(--tan)" stroke-dasharray="0 50 21 29"/>
        <circle cx="28" cy="28" r="21" pathLength="100" stroke="var(--mist)" stroke-dasharray="0 71 15 14"/>
        <circle cx="28" cy="28" r="21" pathLength="100" stroke="var(--sky)" stroke-dasharray="0 86 14 0"/>
      </g>
    </svg>
  </article>

  <article class="process-card abs" style="left:455px">
    <div class="process-cover cover-rest abs" role="img" aria-label="Photo of crossed feet in leather shoes resting outdoors"></div>
    <h3 class="process-title abs">Process Buy A Dount</h3>
    <svg class="process-toggle abs" width="24" height="24" viewBox="0 0 24 24"><circle cx="12" cy="12" r="11" fill="none" stroke="var(--tan)" stroke-width="1.6"/><path d="M7.5 10l4.5 4.5 4.5-4.5" fill="none" stroke="var(--tan)" stroke-width="1.8"/></svg>
    <p class="process-amount tone-tan abs">14 million<br>in expenses</p>
    <p class="process-note abs">Some short free text with<br><a href="#">links</a> and <b>13,432 number</b></p>
    <svg class="process-mix abs" width="56" height="56" viewBox="0 0 56 56">
      <g transform="rotate(-90 28 28)" fill="none" stroke-width="12">
        <circle cx="28" cy="28" r="21" pathLength="100" stroke="var(--navy)" stroke-dasharray="25 75"/>
        <circle cx="28" cy="28" r="21" pathLength="100" stroke="var(--brown)" stroke-dasharray="0 25 25 50"/>
        <circle cx="28" cy="28" r="21" pathLength="100" stroke="var(--tan)" stroke-dasharray="0 50 21 29"/>
        <circle cx="28" cy="28" r="21" pathLength="100" stroke="var(--mist)" stroke-dasharray="0 71 15 14"/>
        <circle cx="28" cy="28" r="21" pathLength="100" stroke="var(--sky)" stroke-dasharray="0 86 14 0"/>
      </g>
    </svg>
  </article>
</section>

<footer class="app-footer abs">
  <div class="footer-brand abs"><span class="brand-dot"></span><span class="brand-name">TOVELU</span></div>
</footer>

</body>
</html>
```